Copper Lantern - responsive bootstrap website design

Looking to build a responsive service website.

Logo has been provided.

PLEASE REVIEW ATTACHED DESIGN STYLE GUIDES & CLIENT CREATIVE BRIEF FOR OUR REQUIREMENT.

THANK YOU AND GOOD LUCK!

Industry/Entity Type

Build

```html
<!DOCTYPE html>
<html lang="en">
<head>
<meta charset="utf-8">
<title>Copper Lantern Outfitters</title>
<link href="https://fonts.googleapis.com/css2?family=Arimo:wght@400;700&display=swap" rel="stylesheet">
<style>
  :root {
    --backdrop: #ececec;
    --topbar: #1f1f1f;
    --teal: #167a6c;
    --teal-dark: #0f5f54;
    --text: #555555;
    --heading-dark: #2b2b2b;
    --khaki: #d4d19c;
    --white: #ffffff;
    --sea-top: #1d2f5e;
    --sea-bottom: #2a4a86;
    --dusk-top: #6d7fa0;
    --dusk-mid: #e0793a;
    --dusk-bottom: #1c2a3c;
  }
  * { box-sizing: border-box; margin: 0; padding: 0; }
  html, body {
    width: 1200px; height: 1023px; overflow: hidden;
    background: var(--backdrop);
    font-family: "Arimo", Arial, sans-serif;
  }
  .page {
    position: absolute; left: 307px; top: 0;
    width: 586px; height: 1023px;
    background: var(--white);
    overflow: hidden;
    box-shadow: 0 0 24px rgba(0,0,0,0.12);
  }
  .topbar {
    position: absolute; top: 0; left: 0; right: 0; height: 46px;
    background: var(--topbar); z-index: 2;
  }
  .brand {
    position: absolute; left: 28px; top: 8px;
    width: 184px; height: 78px;
    background: var(--teal);
    display: flex; align-items: center; justify-content: center;
    color: var(--white); font-size: 21px; font-weight: 400;
    text-align: center; line-height: 1.15;
    z-index: 3;
  }
  .menu-toggle {
    position: absolute; right: 16px; top: 10px;
    width: 26px; height: 26px;
    background: var(--teal-dark); border: 1px solid var(--teal);
  }
  .hero {
    position: absolute; top: 46px; left: 0; right: 0; height: 204px;
    background: linear-gradient(180deg, var(--sea-top), var(--sea-bottom));
  }
  .hero-dots { position: absolute; left: 10px; bottom: 6px; }
  .about {
    position: absolute; top: 250px; left: 0; right: 0; height: 211px;
    text-align: center; padding: 36px 52px 0;
  }
  .about h2 {
    color: var(--teal); font-size: 33px; font-weight: 400; margin-bottom: 14px;
  }
  .about p { color: var(--text); font-size: 15px; line-height: 1.55; }
  .services-banner {
    position: absolute; top: 461px; left: 0; right: 0; height: 100px;
    background: linear-gradient(180deg, var(--dusk-top) 0%, var(--dusk-mid) 55%, var(--dusk-bottom) 100%);
    display: flex; align-items: center; justify-content: center;
  }
  .services-banner h2 {
    color: var(--white); font-size: 33px; font-weight: 400;
  }
  .banner-pointer { position: absolute; left: 272px; bottom: -14px; z-index: 2; }
  .services {
    position: absolute; top: 561px; left: 0; right: 0; bottom: 0;
    background: var(--khaki);
    padding: 40px 54px 0; text-align: center;
  }
  .service { margin-bottom: 36px; }
  .service h3 {
    color: var(--heading-dark); font-size: 15px; font-weight: 700; margin-bottom: 10px;
  }
  .service p { color: var(--text); font-size: 13px; line-height: 1.75; margin-bottom: 12px; }
  .read-more {
    display: inline-block; background: var(--teal); color: var(--white);
    font-size: 11px; padding: 4px 10px;
  }
</style>
</head>
<body>
<main class="page">
  <header class="topbar">
    <div class="menu-toggle"></div>
  </header>
  <div class="brand">Copper Lantern<br>Outfitters</div>

  <section class="hero" role="img" aria-label="Photo of an angler on open water holding a large catch">
    <svg class="hero-dots" width="20" height="6" viewBox="0 0 20 6">
      <circle cx="3" cy="3" r="2.5" fill="#ffffff"/>
      <circle cx="13" cy="3" r="2.5" fill="#ffffff" opacity="0.4"/>
    </svg>
  </section>

  <section class="about">
    <h2>ABOUT US</h2>
    <p>We offer you a very unique fishing experience which is challenging, amid a beautiful setting. Near Atlantic coast beaches and surrounded by beautiful marsh views, Heron Point Island is situated in a wonderful community in peaceful solitude with Live Oaks draped in Spanish Moss.</p>
  </section>

  <section class="services-banner" role="img" aria-label="Sunset over the water with a dock">
    <h2>GUIDE SERVICES</h2>
    <svg class="banner-pointer" width="42" height="16" viewBox="0 0 42 16">
      <polygon points="0,0 42,0 21,16" fill="#c0bd8a"/>
    </svg>
  </section>

  <section class="services">
    <article class="service">
      <h3>Inshore Fishing</h3>
      <p>Lorem ipsum dolor sit amet, consectetuer adipiscing elit, sed diam nonummy nibh euismod tincidunt ut laoreet dolore magna aliquam erat volutpat. Ut wisi enim ad minim veniam, quis nostrud exerci tation ullamcorper suscipit lobortis nisl ut aliquip ex ea commodo consequat.</p>
      <span class="read-more">read more ...</span>
    </article>
    <article class="service">
      <h3>Inshore Fishing</h3>
      <p>Lorem ipsum dolor sit amet, consectetuer adipiscing elit, sed diam nonummy nibh euismod tincidunt ut laoreet dolore magna aliquam erat volutpat. Ut wisi enim ad minim veniam, quis nostrud exerci tation ullamcorper suscipit lobortis nisl ut aliquip ex ea commodo consequat.</p>
      <span class="read-more">read more ...</span>
    </article>
  </section>
</main>
</body>
</html>
```